Tidal Coatings business card for residential and commercial painting

A clean, professional design. Easy to read
Eye catching and elegant
Front could have some color variations
On the back of card I would like all black with signature logo

*Attached is my current business card and the items I want displayed

Contact Information for Business Card

Email, phone number, website, and owner name

Font styles to use
Serif

Requirements
Must have
• My logo with cool design and perhaps some paint splatter

```html
<!DOCTYPE html>
<html lang="en">
<head>
<meta charset="utf-8">
<title>Tidal Coatings — Business Card</title>
<link href="https://fonts.googleapis.com/css2?family=Oswald:wght@500&family=Roboto:wght@400;500&display=swap" rel="stylesheet">
<style>
  :root {
    --backdrop: #6b6667;
    --card-dark: #353537;
    --card-paper: #f1f1f1;
    --rule-grey: #b4b4b4;
    --accent-blue: #0a74bd;
    --text-light: #f4f4f4;
    --mark-grey: #1c1c1e;
  }
  * { box-sizing: border-box; margin: 0; padding: 0; }
  html, body { width: 1200px; height: 1200px; overflow: hidden; }
  body {
    background: var(--backdrop);
    position: relative;
    font-family: "Roboto", Arial, sans-serif;
  }
  .card {
    position: absolute;
    width: 594px;
    height: 349px;
    border-radius: 22px;
    overflow: hidden;
    background: var(--card-dark);
  }
  .card--front { left: 298px; top: 198px; }
  .card--back  { left: 292px; top: 637px; }

  /* front */
  .front-header {
    position: absolute; left: 0; top: 0; width: 100%; height: 210px;
    display: flex; align-items: center; justify-content: center;
  }
  .front-wordmark {
    font-family: "Oswald", "Arial Narrow", sans-serif;
    font-weight: 500;
    font-size: 54px;
    letter-spacing: 0.5px;
    color: var(--mark-grey);
    margin-top: -8px;
  }
  .front-notes {
    position: absolute; left: 0; top: 210px; width: 100%; bottom: 0;
    background: var(--card-paper);
  }
  .note-line {
    position: absolute; left: 35px; right: 35px; height: 2px;
    background: var(--rule-grey);
  }
  .note-line:nth-child(1) { top: 35px; }
  .note-line:nth-child(2) { top: 70px; }
  .note-line:nth-child(3) { top: 105px; }

  /* back */
  .owner { position: absolute; left: 38px; top: 68px; }
  .owner-name {
    font-size: 23px; font-weight: 500; color: var(--accent-blue);
  }
  .owner-title {
    font-size: 15.5px; color: var(--text-light); margin-top: 2px;
  }
  .contact-list {
    position: absolute; left: 38px; top: 200px; list-style: none;
  }
  .contact-item {
    display: flex; align-items: center; gap: 11px;
    font-size: 16px; color: var(--text-light); height: 21px;
  }
  .contact-icon { width: 14px; height: 12px; fill: var(--accent-blue); flex: none; }
  .back-wordmark {
    position: absolute; right: 36px; top: 216px;
    font-family: "Oswald", "Arial Narrow", sans-serif;
    font-weight: 500; font-size: 37px; color: var(--text-light);
    letter-spacing: 0.3px;
  }
  .tagline-band {
    position: absolute; left: 0; bottom: 0; width: 100%; height: 42px;
  }
  .tagline-band svg { position: absolute; left: 0; top: 0; }
  .tagline {
    position: absolute; left: 0; right: 0; top: 14px;
    text-align: center; font-size: 15px; letter-spacing: 5px;
    color: var(--text-light);
  }
</style>
</head>
<body>

<section class="card card--front">
  <div class="front-header">
    <span class="front-wordmark">TIDAL COATINGS</span>
  </div>
  <div class="front-notes">
    <div class="note-line"></div>
    <div class="note-line"></div>
    <div class="note-line"></div>
  </div>
</section>

<section class="card card--back">
  <div class="owner">
    <p class="owner-name">Marcus "MJ"</p>
    <p class="owner-title">Owner - Licensed &amp; Insured</p>
  </div>

  <ul class="contact-list">
    <li class="contact-item">
      <svg class="contact-icon" viewBox="0 0 14 12"><path d="M1 4 Q7 0 13 4 L11 5.5 L9.5 4.2 L4.5 4.2 L3 5.5 Z M3.5 6 L10.5 6 L12 11 L2 11 Z"/></svg>
      555-014-2290
    </li>
    <li class="contact-item">
      <svg class="contact-icon" viewBox="0 0 14 12"><path d="M0 1 H14 V11 H0 Z M1 2 L7 7 L13 2 Z" fill-rule="evenodd"/></svg>
      tidalcoatingsco@mail.com
    </li>
    <li class="contact-item">
      <svg class="contact-icon" viewBox="0 0 14 12"><circle cx="7" cy="6" r="5.5" fill="none" stroke="#0a74bd" stroke-width="1.2"/><path d="M1.5 6 H12.5 M7 0.5 V11.5" stroke="#0a74bd" stroke-width="1" fill="none"/><ellipse cx="7" cy="6" rx="2.5" ry="5.5" fill="none" stroke="#0a74bd" stroke-width="1"/></svg>
      www.tidalcoatingsco.com
    </li>
  </ul>

  <span class="back-wordmark">TIDAL COATINGS</span>

  <div class="tagline-band">
    <svg width="594" height="42" viewBox="0 0 594 42">
      <path fill="#0a74bd" d="M0 5 L40 4 L80 6 L120 3 L170 5 L220 2 L270 4 L320 3 L370 5 L420 2 L470 4 L520 3 L560 1 L594 3 V42 H0 Z"/>
    </svg>
    <p class="tagline">Painted With Pride</p>
  </div>
</section>

</body>
</html>
```